International sports company needs packaging design for color box

We need this box for our yoga mats which we will sell online. This mat is very high quality and 100% environmentally friendly. The yoga mat comes in a stylish yoga bag that will be in the box.

Yoga enthusiasts, athletes, gymnasts, actually all people who do sporting activities and value environmental friendliness will be the contact group

The logo should be visible in any case. The creator is free to choose whether to use only the complete logo or the complete logo with the emblem. In terms of style, it should be reminiscent of a packaging box from Zorvik's Valmox. Be as timeless, modern and elegant as possible. If an environmentally friendly detail can be added, this would certainly be a plus. Color should be black / white / gray.

Target Market(s)

Germany

Requirements
Must have
• Size for the color box should be 13x13x61.5 cm.

```html
<!DOCTYPE html>
<html lang="en">
<head>
<meta charset="utf-8">
<title>Yoga Mat Box – Dieline</title>
<link rel="stylesheet" href="https://fonts.googleapis.com/css2?family=Lato:wght@400;700&family=Questrial&display=swap">
<style>
  :root {
    --bg: #e4e4e4;
    --box-black: #12110f;
    --fold-line: #2c2b28;
    --label-white: #ffffff;
    --ink: #1a1a1a;
    --text-light: #f2f2f2;
    --emblem-grey: #8a8a8a;
  }
  html, body {
    margin: 0;
    padding: 0;
    width: 1200px;
    height: 784px;
    overflow: hidden;
    background: var(--bg);
  }
  .dieline {
    display: block;
    width: 1200px;
    height: 784px;
  }
  .panel { fill: var(--box-black); }
  .fold { stroke: var(--fold-line); stroke-width: 1; stroke-dasharray: 4 3; fill: none; }
  .label-band { fill: var(--label-white); }
  .label-title {
    font-family: "Questrial", sans-serif;
    font-size: 50px;
    letter-spacing: 3px;
    fill: var(--ink);
  }
  .claims {
    font-family: "Lato", sans-serif;
    font-size: 11px;
    fill: var(--text-light);
  }
  .brand-name {
    font-family: "Lato", sans-serif;
    font-weight: 700;
    font-size: 15px;
    letter-spacing: 1.5px;
    fill: var(--text-light);
  }
  .brand-dot { fill: var(--text-light); }
  .eco-emblem { fill: var(--emblem-grey); }
</style>
</head>
<body>
<svg class="dieline" viewBox="30 50 1110 725" preserveAspectRatio="xMidYMid meet" aria-label="Flat dieline of the yoga mat box">
  <!-- lid panel -->
  <g class="box-face face-lid">
    <path class="panel" d="M240,77 H930 L1008,87 Q1022,89 1022,102 V212 Q1022,226 1008,227 L930,236 H240 L161,227 Q147,226 147,212 V102 Q147,89 161,87 Z"/>
    <line class="fold" x1="240" y1="77" x2="240" y2="236"/>
    <line class="fold" x1="930" y1="77" x2="930" y2="236"/>
    <circle class="brand-dot" cx="318" cy="154" r="6"/>
    <text class="brand-name" x="332" y="159">KESTREL</text>
    <text class="claims" text-anchor="middle" x="596" y="141">High quality yoga mat</text>
    <text class="claims" text-anchor="middle" x="596" y="160">100% Environmentally friendly</text>
    <text class="claims" text-anchor="middle" x="596" y="179">Comes in stylish yoga bag</text>
    <circle class="eco-emblem" cx="830" cy="156" r="34" role="img" aria-label="Eco emblem: tree yoga pose with 100% environmentally friendly ring"/>
  </g>

  <!-- front panel with end flaps -->
  <g class="box-face face-front">
    <path class="panel" d="M80,236 H1088 L1106,244 Q1113,247 1113,256 V376 Q1113,385 1106,388 L1088,395 H80 L63,388 Q56,385 56,376 V256 Q56,247 63,244 Z"/>
    <line class="fold" x1="240" y1="236" x2="930" y2="236"/>
    <line class="fold" x1="240" y1="236" x2="240" y2="395"/>
    <line class="fold" x1="930" y1="236" x2="930" y2="395"/>
    <rect class="label-band" x="410" y="271" width="359" height="91"/>
    <text class="label-title" text-anchor="middle" x="590" y="334">YOGA MAT</text>
    <circle class="eco-emblem" cx="165" cy="315" r="34" role="img" aria-label="Eco emblem: tree yoga pose with 100% environmentally friendly ring"/>
  </g>

  <!-- back panel -->
  <g class="box-face face-back">
    <path class="panel" d="M240,395 H930 L1008,405 Q1022,407 1022,420 V530 Q1022,544 1008,545 L930,553 H240 L161,545 Q147,544 147,530 V420 Q147,407 161,405 Z"/>
    <line class="fold" x1="240" y1="395" x2="930" y2="395"/>
    <line class="fold" x1="240" y1="395" x2="240" y2="553"/>
    <line class="fold" x1="930" y1="395" x2="930" y2="553"/>
    <circle class="brand-dot" cx="318" cy="473" r="6"/>
    <text class="brand-name" x="332" y="478">KESTREL</text>
    <text class="claims" text-anchor="middle" x="596" y="461">High quality yoga mat</text>
    <text class="claims" text-anchor="middle" x="596" y="480">100% Environmentally friendly</text>
    <text class="claims" text-anchor="middle" x="596" y="499">Comes in stylish yoga bag</text>
    <circle class="eco-emblem" cx="830" cy="475" r="34" role="img" aria-label="Eco emblem: tree yoga pose with 100% environmentally friendly ring"/>
  </g>

  <!-- base panel with glue strip -->
  <g class="box-face face-base">
    <path class="panel" d="M240,553 H930 V713 L926,730 Q922,740 910,740 H260 Q248,740 244,730 L240,713 Z"/>
    <line class="fold" x1="240" y1="553" x2="930" y2="553"/>
    <line class="fold" x1="240" y1="713" x2="930" y2="713"/>
    <rect class="label-band" x="410" y="587" width="359" height="90"/>
    <text class="label-title" text-anchor="middle" x="590" y="649">YOGA MAT</text>
  </g>
</svg>
</body>
</html>
```